Fancy looking Inspection Postcard

Postcard needed for customers to inspect their product once it is delivered. We'll be giving them the steps for inspecting their product and to contact us if any issues arise. Would like to see something that sticks out but uses our company's colors. Would like to see creativity. Possibly utilizing the diamond steel background like we have in our logo.

Target Market(s)

Customers of our manufacturing shop

Industry/Entity Type

Manufacturing - metal wall art, custom products

Requirements
Must have
• our colors and logo
Nice to have
• get creative. i like creativity

```html
<!DOCTYPE html>
<html lang="en">
<head>
<meta charset="UTF-8">
<title>Customer Inspection Checklist – Iron Bend Fabrication</title>
<link href="https://fonts.googleapis.com/css2?family=Oswald:wght@500;600;700&family=Roboto+Condensed:wght@400&display=swap" rel="stylesheet">
<style>
  :root{
    --green-deep:#4e7f4f;
    --green-mid:#6f9a5d;
    --gold:#d6cf8c;
    --olive:#93995f;
    --pill-green:#76a043;
    --yellow:#fff200;
    --black:#050505;
    --white:#ffffff;
    --silver-dark:#8e8e8e;
    --silver-light:#f4f4f4;
    --accent-green:#76a043;
  }
  *{box-sizing:border-box;margin:0;padding:0}
  html,body{width:1200px;height:800px;overflow:hidden}
  body{
    position:relative;
    background:linear-gradient(90deg,var(--green-deep) 0%,var(--green-mid) 18%,var(--gold) 34%,var(--olive) 58%,var(--green-mid) 78%,var(--green-deep) 100%);
    font-family:"Roboto Condensed",sans-serif;
    color:var(--white);
  }
  .checklist-panel{
    position:absolute;left:73px;top:120px;width:1140px;height:418px;
    border-left:7px solid var(--silver-light);
    border-bottom:7px solid var(--silver-light);
    border-bottom-left-radius:200px;
    background:radial-gradient(ellipse at 60% 40%,#1d1d1d 0%,#0b0b0b 60%,var(--black) 100%);
    box-shadow:-2px 3px 0 var(--silver-dark);
  }
  .title-bar{
    position:absolute;left:240px;top:60px;width:960px;height:81px;
    background:linear-gradient(90deg,#9c9c9c 0%,#e9e9e9 15%,#bdbdbd 35%,var(--silver-light) 60%,#a9a9a9 80%,var(--silver-light) 90%,#9a9a9a 100%);
    display:flex;align-items:center;justify-content:center;
  }
  .title-bar h1{
    font-family:"Oswald",sans-serif;font-weight:700;font-size:44px;
    color:var(--black);letter-spacing:0.5px;transform:scaleX(0.9);margin-left:26px;
  }
  .brand-name{
    position:absolute;left:48px;top:150px;width:200px;
    font-family:"Oswald",sans-serif;font-weight:600;font-size:28px;line-height:1.05;
    color:var(--yellow);text-align:center;
  }
  .step{position:absolute;width:400px}
  .step h2{
    font-family:"Oswald",sans-serif;font-weight:500;font-size:23px;color:var(--yellow);
    display:flex;align-items:baseline;gap:6px;
  }
  .step h2 .num{font-size:44px;font-weight:600;line-height:1}
  .step ul{list-style:none;margin:4px 0 0 27px}
  .step li{font-size:24px;line-height:30px}
  .step li::before{content:"• ";}
  .step-1{left:297px;top:185px}
  .step-2{left:716px;top:185px}
  .step-3{left:297px;top:331px}
  .step-4{left:716px;top:331px}
  .contact-pill{
    position:absolute;left:302px;top:500px;width:763px;height:80px;
    background:var(--pill-green);border:4px solid var(--silver-light);border-radius:40px;
    box-shadow:0 3px 0 var(--silver-dark);
    display:flex;flex-direction:column;align-items:center;justify-content:center;
    font-family:"Oswald",sans-serif;font-weight:500;font-size:20px;line-height:27px;color:#f3f7e8;
  }
  .feedback-band{
    position:absolute;left:-10px;top:617px;width:1150px;height:148px;
    background:var(--black);
    border-top:13px solid var(--silver-light);
    border-right:7px solid var(--silver-light);
    border-bottom:7px solid var(--silver-light);
    border-bottom-right-radius:48px;
    box-shadow:2px 3px 0 var(--silver-dark);
  }
  .feedback-text{position:absolute;font-size:24px;line-height:30px}
  .feedback-line-1{left:60px;top:659px}
  .feedback-line-2{left:290px;top:697px}
  .feedback-text em{font-family:"Oswald",sans-serif;font-weight:500;font-style:italic}
  .hl-yellow{color:var(--yellow)}
  .hl-green{color:var(--accent-green)}
  .review-icon{position:absolute;left:1067px;top:587px;width:96px;height:96px}
</style>
</head>
<body>
  <div class="checklist-panel" role="img" aria-label="Black diamond-plate steel texture"></div>
  <header class="title-bar"><h1>CUSTOMER INSPECTION CHECKLIST</h1></header>
  <div class="brand-name">IRON BEND FABRICATION</div>

  <section class="step step-1">
    <h2><span class="num">1.</span> Inspect general shape</h2>
    <ul><li>Is it what you expected</li><li>Is it bent, disoriented?</li></ul>
  </section>
  <section class="step step-2">
    <h2><span class="num">2.</span> Inspect the welds if there are any</h2>
    <ul><li>Do they look clean?</li><li>Are there any gaps?</li></ul>
  </section>
  <section class="step step-3">
    <h2><span class="num">3.</span> Inspect the finish</h2>
    <ul><li>Are there any areas not finished?</li><li>Are the colors what you expected?</li></ul>
  </section>
  <section class="step step-4">
    <h2><span class="num">4.</span> Check for functionality</h2>
    <ul><li>Does it work the way you want it to?</li><li>Is it what you expected?</li></ul>
  </section>

  <div class="contact-pill">
    <span>Email us at orders@ironbendfab.com, shoot us a text (208) 555-0142,</span>
    <span>or reach out via www.ironbendfab.com/contact</span>
  </div>

  <div class="feedback-band"></div>
  <p class="feedback-text feedback-line-1"><em class="hl-yellow">Did we do a good job?</em> If you think so, leave us a review on Searchly?</p>
  <p class="feedback-text feedback-line-2">If not, Please let us know - <em class="hl-green">info@ironbendfab.com or call us 208-555-0187</em></p>

  <svg class="review-icon" viewBox="0 0 96 96" aria-hidden="true">
    <circle cx="48" cy="48" r="44" fill="#000" stroke="var(--yellow)" stroke-width="6"/>
    <g fill="none" stroke="var(--yellow)" stroke-width="3.5" stroke-linecap="round" stroke-linejoin="round">
      <path d="M58 30H26a4 4 0 0 0-4 4v24a4 4 0 0 0 4 4h36a4 4 0 0 0 4-4v-8"/>
      <line x1="22" y1="38" x2="50" y2="38"/>
      <line x1="28" y1="45" x2="46" y2="45"/>
      <line x1="28" y1="52" x2="42" y2="52"/>
      <path d="M70 26l5 5-20 20-7 2 2-7z"/>
    </g>
    <g fill="var(--yellow)"><circle cx="27" cy="34" r="1.3"/><circle cx="31" cy="34" r="1.3"/><circle cx="35" cy="34" r="1.3"/></g>
  </svg>
</body>
</html>
```